Larkmoor Dental Center Specials/Offers

Take the advertisement pic (LABELED ADVERTISEMENT) and make it look "professional in appearance" using the logo and color scheme of Larkmoor Dental Center. The Phone number should be 614-382-2096. I want the same content, different background, professional looking document. I want it to be a 12"x12" document. High resolution files should include .PDF, .JPG and .AI. Any or all documents can be used for colors and overall scheme. I would like to have the overall colors include the main blue color from the file 4db749b4ef4c5e0717512bf7eb26bf54 and include the brown "swoosh" somewhere through/on the final document. Stock files of smiling young families can be used but not required. I am on a tight time-line and have placed 5 days as the deadline, but I will pick my favorite in as little as 2-3 days if I can get a good product. Again ALL the info from the Advertisement document should be included on the final product. Use any or all of the uploaded files for assistance. You can also visit our website for more info: www.larkmoordentalcenter.example Thanks

```html
<!DOCTYPE html>
<html lang="en">
<head>
<meta charset="utf-8">
<title>Larkmoor Dental Center – Specials and Offers</title>
<link rel="stylesheet" href="https://fonts.googleapis.com/css2?family=Tinos:wght@400;700&family=Archivo+Black&family=Libre+Baskerville:wght@700&family=Oswald:wght@400;500&family=Montserrat:wght@500&display=swap">
<style>
  :root{
    --frame:#0d0d0d;
    --sky-light:#9fb6c6;
    --sky-mid:#4f7f95;
    --sky-dark:#1d4c60;
    --panel:#c9c9c9;
    --panel-edge:#8a8a8a;
    --ink:#111111;
    --logo-box:#3b3b3b;
    --logo-text:#c9a28f;
    --headline:#4a4f53;
    --hex:#3d4347;
    --ground:#c8c8c8;
    --ground-light:#e3e3e3;
    --band:#121212;
    --doctor:#5a4a3f;
  }
  *{margin:0;padding:0;box-sizing:border-box}
  html,body{width:1200px;height:1200px;overflow:hidden;background:#ffffff}
  .ad{position:relative;width:1200px;height:1200px;border:14px solid var(--frame);overflow:hidden;font-family:"Tinos",serif;color:var(--ink)}
  .backdrop{position:absolute;inset:0;width:100%;height:100%}
  .logo{position:absolute;left:4px;top:4px;width:545px;height:250px;background:var(--logo-box);
        display:flex;align-items:center;gap:26px;padding-left:44px}
  .logo-mark{width:60px;height:60px;border-radius:50%;background:var(--logo-text);flex:none}
  .logo-text{font-family:"Montserrat",sans-serif;font-weight:500;color:var(--logo-text);line-height:1.25}
  .logo-name{font-size:40px}
  .logo-tag{font-size:21px;letter-spacing:2px;margin-top:10px}
  .headline{position:absolute;left:620px;top:62px;width:500px;text-align:center;white-space:nowrap;
            font-family:"Libre Baskerville",serif;font-weight:700;font-size:34px;line-height:1.45;
            letter-spacing:-1px;color:var(--headline);transform:rotate(7deg)}
  .panel{position:absolute;background:var(--panel);border:3px solid var(--panel-edge);text-align:center}
  .providers{left:26px;top:278px;width:556px;height:246px;padding-top:14px}
  .providers h2{font-weight:400;font-size:34px;margin-bottom:16px}
  .providers .plans{font-size:27px;line-height:1.3}
  .providers .note{font-size:22px;margin-top:18px}
  .new-patient{left:596px;top:278px;width:547px;height:246px;padding-top:10px}
  .new-patient p{font-size:32px;line-height:1.3}
  .fine{font-size:19px;margin-top:8px}
  .discount{left:333px;top:564px;width:508px;height:212px;padding-top:6px}
  .discount .big{font-family:"Archivo Black",sans-serif;font-size:62px;letter-spacing:2px;line-height:1.15}
  .discount p{font-size:32px;line-height:1.2}
  .hex{position:absolute;width:256px;height:222px;display:flex;align-items:center;justify-content:center;
       text-align:center;font-size:25px;line-height:1.3;color:var(--ink)}
  .hex svg{position:absolute;inset:0;width:100%;height:100%}
  .hex span{position:relative}
  .hex-referral{left:34px;top:536px}
  .hex-bleach{left:888px;top:545px}
  .call{position:absolute;left:20px;top:1000px;width:300px;text-align:center;line-height:1.5}
  .call .lead{font-weight:700;font-size:36px}
  .call .sub{font-size:34px}
  .call .phone{font-size:36px}
  .web{position:absolute;left:350px;top:1128px;font-size:30px;white-space:nowrap}
  .office{position:absolute;right:18px;top:995px;text-align:center;white-space:nowrap;
          font-family:"Oswald",sans-serif;line-height:1.55}
  .office .doctor{font-size:29px;color:var(--doctor);letter-spacing:0.5px}
  .office .addr{font-size:28px;color:var(--ink)}
</style>
</head>
<body>
<div class="ad">
  <svg class="backdrop" viewBox="0 0 1172 1172" preserveAspectRatio="none" aria-hidden="true">
    <defs>
      <linearGradient id="sky" x1="0" y1="0" x2="1" y2="0.3">
        <stop offset="0" stop-color="var(--sky-light)"/>
        <stop offset="0.5" stop-color="var(--sky-mid)"/>
        <stop offset="1" stop-color="var(--sky-dark)"/>
      </linearGradient>
      <linearGradient id="ground" x1="0" y1="0" x2="0" y2="1">
        <stop offset="0" stop-color="var(--ground-light)"/>
        <stop offset="1" stop-color="var(--ground)"/>
      </linearGradient>
    </defs>
    <rect width="1172" height="1172" fill="url(#sky)"/>
    <path d="M0,790 C260,780 520,850 1172,950 L1172,1000 C700,950 300,870 0,895 Z" fill="var(--band)"/>
    <path d="M0,895 C300,870 700,950 1172,1000 L1172,1172 L0,1172 Z" fill="url(#ground)"/>
    <path d="M0,905 C300,882 700,960 1172,1010" fill="none" stroke="#f2f2f2" stroke-width="4"/>
  </svg>

  <div class="logo">
    <div class="logo-mark"></div>
    <div class="logo-text">
      <div class="logo-name">Larkmoor Dental Center</div>
      <div class="logo-tag">FAMILY · COSMETIC · IMPLANTS</div>
    </div>
  </div>

  <div class="headline">Where The Whole Family<br>Can Be Seen</div>

  <section class="panel providers">
    <h2>Preferred Provider For:</h2>
    <div class="plans">Harbor Dental, Northline, Crestpoint, Veralis<br>SS/BP and Allied Meridian</div>
    <div class="note">We take all other non-HMO plans</div>
  </section>

  <section class="panel new-patient">
    <p>$59 New Patients</p>
    <p>X-Rays</p>
    <p>Comprehensive Exam</p>
    <p>Regular Cleaning</p>
    <div class="fine">- Only Patients with Dental Benefits</div>
  </section>

  <div class="hex hex-referral">
    <svg viewBox="0 0 256 222" aria-hidden="true"><polygon points="64,0 192,0 256,111 192,222 64,222 0,111" fill="var(--hex)"/></svg>
    <span>Ask about<br>our<br>Referral<br>Program</span>
  </div>

  <section class="panel discount">
    <div class="big">20% OFF</div>
    <p>Treatment scheduled<br>on your first visit.</p>
    <div class="fine">- Only Patients with Dental Benefits</div>
  </section>

  <div class="hex hex-bleach">
    <svg viewBox="0 0 256 222" aria-hidden="true"><polygon points="64,0 192,0 256,111 192,222 64,222 0,111" fill="var(--hex)"/></svg>
    <span>$99<br>Bleaching<br>Special</span>
  </div>

  <div class="call">
    <div class="lead">CALL TODAY</div>
    <div class="sub">for an Appointment</div>
    <div class="phone">(614) 382-2096</div>
  </div>

  <div class="web">www.larkmoordentalcenter.example</div>

  <div class="office">
    <div class="doctor">DANIEL R. HOLLIS&nbsp;&nbsp;D.D.S.</div>
    <div class="addr">2240 Alder Ridge Dr. Suite B</div>
    <div class="addr">Westbrook, OH 43217</div>
  </div>
</div>
</body>
</html>
```